Mindfulness School for Children -- Business Cards

We're looking for business cards for our school directors and owners. We're a mindfulness school for children called little compass. Attached are our logos/icons.

```html
<!DOCTYPE html>
<html lang="en">
<head>
<meta charset="utf-8">
<title>little compass — Business Cards</title>
<link rel="stylesheet" href="https://fonts.googleapis.com/css2?family=Source+Sans+3:wght@400;600;700&display=swap">
<style>
  :root {
    --backdrop: #2c2f36;
    --teal: #0f8a98;
    --teal-deep: #2f8ea6;
    --sea: #4f9bb0;
    --leaf: #8cc79a;
    --paper: #e9eaef;
    --ink: #23262c;
    --rule: #9a9ca3;
    --white: #f3f4f6;
  }
  * { box-sizing: border-box; margin: 0; padding: 0; }
  html, body {
    width: 1200px; height: 1000px; overflow: hidden;
    background: var(--backdrop);
    font-family: "Source Sans 3", Arial, sans-serif;
  }
  .sheet {
    position: relative; width: 1200px; height: 1000px;
  }
  .card {
    position: absolute; left: 220px; width: 760px; height: 434px;
    border-radius: 26px; overflow: hidden;
  }
  .card--front { top: 48px; background: var(--teal); }
  .card--back  { top: 518px; background: var(--paper); }

  /* front */
  .front-brand {
    position: absolute; left: 0; right: 0; top: 150px;
    text-align: center; color: var(--white);
    font-size: 74px; font-weight: 400; letter-spacing: 0.5px; line-height: 1;
  }
  .front-web {
    position: absolute; left: 0; right: 0; top: 292px;
    text-align: center; color: var(--white);
    font-size: 17px; letter-spacing: 1.6px;
  }

  /* back */
  .back-brand {
    position: absolute; left: 108px; top: 96px;
    color: var(--teal-deep);
    font-size: 62px; font-weight: 400; line-height: 1;
  }
  .person { position: absolute; right: 70px; top: 150px; text-align: left; }
  .person__name {
    color: var(--teal-deep); font-weight: 700; font-size: 24px; letter-spacing: 0.3px;
  }
  .person__role {
    color: var(--ink); font-size: 17px; margin-left: 62px; margin-top: -2px;
  }
  .divider {
    position: absolute; left: 150px; top: 198px; width: 410px; height: 1px; background: var(--rule);
  }
  .address {
    position: absolute; left: 96px; top: 232px;
    color: var(--ink); font-size: 17px; line-height: 1.3;
  }
  .address-rule {
    position: absolute; left: 96px; top: 287px; width: 160px; height: 1px; background: var(--rule);
  }
  .contacts {
    position: absolute; left: 96px; top: 298px; list-style: none;
    color: var(--ink); font-size: 17px; line-height: 1.35;
  }
  .contacts li { display: flex; align-items: center; gap: 10px; }
  .contacts svg { width: 13px; height: 13px; flex: none; }
  .swoosh { position: absolute; left: 0; top: 0; width: 760px; height: 434px; }
</style>
</head>
<body>
<main class="sheet">

  <section class="card card--front" aria-label="Card front">
    <p class="front-brand">littlecompass</p>
    <p class="front-web">www.littlecompass.org</p>
  </section>

  <section class="card card--back" aria-label="Card back">
    <svg class="swoosh" viewBox="0 0 760 434" aria-hidden="true">
      <path d="M0 434 C 300 420, 600 330, 760 150 L 760 434 Z" fill="var(--sea)"/>
      <path d="M300 410 C 520 360, 660 270, 760 128" fill="none" stroke="var(--leaf)" stroke-width="5"/>
    </svg>

    <p class="back-brand">littlecompass</p>

    <div class="person">
      <p class="person__name">CLARA WHITFIELD</p>
      <p class="person__role">Managing Director</p>
    </div>
    <div class="divider"></div>

    <p class="address">240 Juniper Lane Fairhaven<br>OR 97035, United States</p>
    <div class="address-rule"></div>

    <ul class="contacts">
      <li>
        <svg viewBox="0 0 16 16"><path d="M4 1.5 L6.5 4.5 L5 6 C6 8.5 7.5 10 10 11 L11.5 9.5 L14.5 12 L12.5 14.5 C7 14 2 9 1.5 3.5 Z" fill="var(--teal-deep)"/></svg>
        +1 555.010.2040
      </li>
      <li>
        <svg viewBox="0 0 16 16"><rect x="1" y="3" width="14" height="10" fill="var(--teal-deep)"/><path d="M1 3 L8 9 L15 3" fill="none" stroke="var(--paper)" stroke-width="1.3"/></svg>
        info@littlecompass.org
      </li>
      <li>
        <svg viewBox="0 0 16 16"><circle cx="8" cy="8" r="6.5" fill="none" stroke="var(--teal-deep)" stroke-width="1.4"/><ellipse cx="8" cy="8" rx="2.8" ry="6.5" fill="none" stroke="var(--teal-deep)" stroke-width="1.2"/><line x1="1.5" y1="8" x2="14.5" y2="8" stroke="var(--teal-deep)" stroke-width="1.2"/></svg>
        www.littlecompass.org
      </li>
    </ul>
  </section>

</main>
</body>
</html>
```